Business card design reauest

2 sided. White on both sides

Martin Oakhurst

Ho Chi Minh, Vietnam

Cell Phone / Whatsapp/ Wechat/Zalo
1-555-382-7194
Moakhurst@kvpartsline.vn
Www.kvpartsline.vn
Www.kvpartsline.com

Industry/Entity Type

Sofa and furniture and kitchen

Contact Information for Business Card

2 sided. White on both sides Martin Oakhurst Ho Chi Minh, Vietnam Cell Phone / Whatsapp/ Wechat/Zalo 1-555-382-7194 Moakhurst@kvpartsline.vn Www.kvpartsline.vn Www.kvpartsline.com

```html
<!DOCTYPE html>
<html lang="en">
<head>
<meta charset="utf-8">
<title>KV Partsline – Business Card</title>
<link href="https://fonts.googleapis.com/css2?family=Cinzel:wght@500&family=Poppins:wght@400&display=swap" rel="stylesheet">
<style>
  :root {
    --brand-green: #009a3d;
    --green-tint: #d8efe0;
    --green-tint-soft: #eef8f1;
    --ink: #231f20;
    --paper: #ffffff;
    --backdrop: #e6e6e6;
  }
  * { box-sizing: border-box; margin: 0; padding: 0; }
  html, body { width: 1200px; height: 1200px; overflow: hidden; }
  body {
    background: var(--backdrop);
    position: relative;
    font-family: "Poppins", sans-serif;
  }
  .card {
    position: absolute;
    top: 246px;
    width: 440px;
    height: 708px;
    background: var(--paper);
    box-shadow: 0 2px 6px rgba(0,0,0,0.18);
    overflow: hidden;
  }
  .card--front { left: 140px; }
  .card--back { left: 620px; }

  .front-wordmark {
    position: absolute;
    left: 0; right: 0;
    top: 394px;
    text-align: center;
    font-family: "Cinzel", serif;
    font-weight: 500;
    font-size: 50px;
    line-height: 1;
    letter-spacing: 1px;
    color: var(--brand-green);
  }

  .motif-area {
    position: absolute;
    left: 8px;
    right: 8px;
  }
  .motif-area--top {
    top: 0;
    height: 156px;
    background: linear-gradient(180deg, var(--green-tint) 0%, var(--green-tint-soft) 100%);
  }
  .motif-area--bottom {
    bottom: 0;
    height: 170px;
    background: linear-gradient(0deg, var(--green-tint) 0%, var(--green-tint-soft) 100%);
  }

  .contact-panel {
    position: absolute;
    left: 40px;
    top: 225px;
    width: 358px;
    height: 318px;
    background: var(--brand-green);
    color: var(--paper);
    text-align: center;
    display: flex;
    flex-direction: column;
    align-items: center;
    padding-top: 24px;
  }
  .contact-name {
    font-family: "Cinzel", serif;
    font-weight: 500;
    font-size: 23px;
    line-height: 1.2;
    letter-spacing: 0.5px;
  }
  .divider {
    width: 58px;
    height: 1px;
    background: var(--paper);
    margin: 14px 0 15px;
  }
  .contact-city { font-size: 17px; line-height: 1.2; }
  .channel-icons {
    display: flex;
    gap: 4px;
    margin-bottom: 8px;
  }
  .channel-icons svg { width: 26px; height: 26px; display: block; }
  .contact-phone { font-size: 17px; line-height: 1.2; letter-spacing: 0.5px; }
  .contact-lines { font-size: 16.5px; line-height: 28px; margin-top: -2px; }
</style>
</head>
<body>
  <section class="card card--front">
    <div class="front-wordmark">KV PARTSLINE</div>
  </section>

  <section class="card card--back">
    <div class="motif-area motif-area--top" role="img" aria-label="Decorative roof line with hanging lamp"></div>
    <div class="motif-area motif-area--bottom" role="img" aria-label="Decorative table and chairs"></div>

    <div class="contact-panel">
      <div class="contact-name">MARTIN OAKHURST</div>
      <div class="divider"></div>
      <div class="contact-city">Ho Chi Minh, Vietnam</div>
      <div class="divider"></div>
      <div class="channel-icons">
        <svg viewBox="0 0 26 26" aria-label="Cell phone">
          <circle cx="13" cy="13" r="12" fill="none" stroke="#fff" stroke-width="1.3"/>
          <rect x="9.5" y="6.5" width="7" height="13" rx="1.2" fill="none" stroke="#fff" stroke-width="1.2"/>
          <circle cx="13" cy="17.2" r="0.8" fill="#fff"/>
        </svg>
        <svg viewBox="0 0 26 26" aria-label="Chat">
          <circle cx="13" cy="13" r="12" fill="none" stroke="#fff" stroke-width="1.3"/>
          <path d="M7.5 8.5h11v7h-6l-3 2.5v-2.5h-2z" fill="none" stroke="#fff" stroke-width="1.2" stroke-linejoin="round"/>
        </svg>
        <svg viewBox="0 0 26 26" aria-label="Message">
          <circle cx="13" cy="13" r="12" fill="none" stroke="#fff" stroke-width="1.3"/>
          <rect x="7" y="8.5" width="12" height="9" rx="1" fill="none" stroke="#fff" stroke-width="1.2"/>
          <path d="M7.3 9l5.7 4.5L18.7 9" fill="none" stroke="#fff" stroke-width="1.2"/>
        </svg>
        <svg viewBox="0 0 26 26" aria-label="Messenger">
          <circle cx="13" cy="13" r="12" fill="none" stroke="#fff" stroke-width="1.3"/>
          <circle cx="9" cy="13" r="1.2" fill="#fff"/>
          <circle cx="13" cy="13" r="1.2" fill="#fff"/>
          <circle cx="17" cy="13" r="1.2" fill="#fff"/>
        </svg>
      </div>
      <div class="contact-phone">1-555-382-7194</div>
      <div class="divider"></div>
      <div class="contact-lines">
        <div>Moakhurst@kvpartsline.vn</div>
        <div>Www.kvpartsline.vn</div>
        <div>Www.kvpartsline.com</div>
      </div>
    </div>
  </section>
</body>
</html>
```